Global Developmental Delay Awareness Day Poster

I need a poster to raise awareness for a condition called Global Developmental Delay (GDD) . The day of awareness for this condition is May 1. The condition is something found in children who are significantly delayed in their milestones. We are hopeful that through education and support more children with this condition can gain access to therapies and support to minimize the long term effects and maxamise their potential. Theme for GDD awareness is yellow so lots of yellow needed. Can be any yellow. Like it to be colourful, but not bright if that makes sense. I'd like it to be classy but fun and childish - this is a childhood diagnosis. Just not 'tacky'. Like the design to reflect the wonders of childhood so feel free to use your imagination!

Target Market(s)

Mums (and dads) of young children under 5

Colors
fee18a
fbf289

Requirements
Must have
• cheery, childish, happy feel - see uploaded poster examples for ideas. They are just ideas for theme. Different fun, childish fonts and 'sections' - perhaps with different colour backgrounds etc.
• Heading should be "Global Developmental Delay" or something similar
• Must have text as in the attachment
• Must have yellow 'theme'
• more colours than just yellow.
Nice to have
• colors - not bright but colorful.

```html
<!DOCTYPE html>
<html lang="en">
<head>
<meta charset="utf-8">
<title>Global Developmental Delay Awareness Poster</title>
<link href="https://fonts.googleapis.com/css2?family=Abril+Fatface&family=Alfa+Slab+One&family=Anton&family=Bangers&family=Cutive+Mono&family=Lobster+Two:ital,wght@1,700&family=Nunito:wght@800&family=Oswald:wght@500&family=PT+Sans+Narrow&family=Permanent+Marker&family=Playfair+Display:ital,wght@1,700&family=Rubik:wght@700;900&display=swap" rel="stylesheet">
<style>
:root{
  --cream:#fef1b8;
  --grey:#8a8583;
  --lavender:#b9b8f0;
  --plum:#3e1a5c;
  --magenta:#e5198a;
  --sky:#93d3f9;
  --navy:#1c5a96;
  --apricot:#fdc770;
  --sun:#ffcc00;
  --gold:#f5c33b;
  --orange:#f47f24;
  --ink:#3a2a10;
  --stone:#7d7572;
  --white:#ffffff;
}
*{margin:0;padding:0;box-sizing:border-box}
html,body{width:849px;height:1200px;overflow:hidden;background:var(--cream)}
.poster{position:relative;width:849px;height:1200px;background:var(--cream);overflow:hidden;font-family:'Nunito',sans-serif}
.abs{position:absolute;white-space:nowrap}
.shapes{position:absolute;left:0;top:0}

/* WHAT panel */
.what-letters{left:20px;top:38px;width:44px;font-family:'Rubik',sans-serif;font-weight:900;font-size:46px;line-height:50px;color:var(--sun);-webkit-text-stroke:2px var(--orange);text-align:center}
.tag{background:var(--gold);color:var(--grey);font-family:'Rubik',sans-serif;font-weight:700;font-size:30px;padding:2px 10px;line-height:40px}
.tag-1{left:92px;top:14px}
.tag-2{left:92px;top:70px}
.what-line{left:90px;font-family:'Cutive Mono',monospace;color:var(--white);text-transform:uppercase;line-height:1}
.what-line .hl{color:var(--sky)}
.wl-1{top:138px;font-size:19.5px}
.wl-2{top:164px;font-size:19.5px}
.wl-3{top:189px;font-size:26.5px}
.wl-4{top:221px;font-size:41px}
.wl-5{top:266px;font-size:27.5px}

/* Causes */
.causes-title{left:598px;top:12px;font-family:'Lobster Two',cursive;font-style:italic;font-weight:700;font-size:70px;color:#6b6bd6;-webkit-text-stroke:2px var(--white)}
.cause{left:612px;font-family:'Anton',sans-serif;color:var(--plum);text-transform:uppercase;line-height:1}
.pill{font-family:'Permanent Marker',cursive;background:var(--magenta);color:var(--white);padding:0 3px;letter-spacing:2px}
.k1{top:106px;font-size:24px}
.k1 .pill{font-size:15px}
.k2{top:128px;font-size:35px}
.k3{top:162px;font-size:34px}
.k3 .pill{font-size:22px;letter-spacing:3px}
.k4{top:192px;font-size:54px}
.k5{top:243px;font-size:33px}
.k6{top:272px;font-size:74px}
.k7{top:342px;font-size:29px}
.k7 .pill{font-size:19px}
.k8{top:370px;font-size:41px}

/* headline */
.headline{font-family:'Bangers',cursive;color:var(--gold);text-shadow:2px 2px 0 var(--ink),4px 4px 0 var(--ink);-webkit-text-stroke:1px var(--ink);letter-spacing:4px;line-height:1}
.h-child{left:190px;top:298px;font-size:80px}
.h-help{left:120px;top:676px;font-size:80px}
.h-needs{left:530px;top:392px;font-size:62px;line-height:63px;width:60px;text-align:center;letter-spacing:0}

/* GDD box */
.gdd-box{left:18px;top:372px;width:250px;height:296px;border:4px dashed var(--navy);border-right:none}
.gdd-text{left:28px;top:380px;font-size:21px;line-height:28.5px;color:var(--white);font-weight:800}
.gdd-text b{font-family:'Alfa Slab One',serif;font-weight:400;color:var(--navy)}
.realms{left:334px;top:382px;font-family:'Oswald',sans-serif;font-weight:500;color:var(--navy);font-size:24px}
.realms li{list-style:none;height:64px;line-height:44px}
.icon-dot{fill:var(--navy)}

/* What can you do */
.wcyd-title{left:610px;top:606px;width:226px;font-family:'Playfair Display',serif;font-style:italic;font-weight:700;font-size:39px;line-height:46px;color:var(--stone);-webkit-text-stroke:1px var(--white);text-align:center}
.wcyd-text{left:565px;top:718px;font-family:'PT Sans Narrow',sans-serif;font-size:17.5px;line-height:24.6px;color:var(--ink)}
.wcyd-text b{font-family:'Abril Fatface',serif;font-weight:400;color:var(--stone)}

/* concerned */
.concerned{left:16px;top:1178px;transform:rotate(-90deg);transform-origin:left top;font-family:'Rubik',sans-serif;font-weight:900;font-size:40px;color:var(--orange);letter-spacing:1px}
.concerned-text{left:78px;top:858px;color:var(--white);font-weight:800;font-size:28px;line-height:32px}
.concerned-text em{font-family:'Permanent Marker',cursive;font-style:normal;color:var(--gold);font-size:25px;letter-spacing:2px}

/* info */
.info-title{left:444px;top:922px;font-family:'Playfair Display',serif;font-style:italic;font-weight:700;font-size:24px;color:#8a6a10;text-shadow:1px 1px 0 var(--ink)}
</style>
</head>
<body>
<main class="poster">
  <svg class="shapes" width="849" height="1200" viewBox="0 0 849 1200">
    <rect x="0" y="0" width="545" height="335" fill="var(--grey)"/>
    <polygon points="555,0 849,0 849,410 735,600 555,405" fill="var(--lavender)"/>
    <polygon points="540,360 555,405 735,600 849,410 849,910 540,910" fill="var(--apricot)"/>
    <rect x="0" y="355" width="528" height="335" fill="var(--sky)"/>
    <polygon points="0,770 185,690 365,770 365,1185 0,1185" fill="var(--grey)"/>
    <rect x="385" y="920" width="440" height="260" fill="var(--sun)"/>
    <g class="icon-dot">
      <circle cx="292" cy="395" r="20"/>
      <circle cx="292" cy="460" r="8"/><circle cx="270" cy="448" r="5"/><circle cx="314" cy="448" r="5"/><circle cx="270" cy="472" r="5"/><circle cx="314" cy="472" r="5"/>
      <circle cx="289" cy="518" r="7"/><rect x="282" y="526" width="14" height="26" rx="4"/>
      <path d="M272 598 h30 l10 -8 v12 h-40z"/>
      <circle cx="300" cy="628" r="7"/><rect x="292" y="636" width="14" height="26" rx="4"/><circle cx="307" cy="678" r="8"/>
    </g>
  </svg>

  <div class="abs" role="img" aria-label="lightning bolt doodles" style="left:470px;top:28px;width:56px;height:48px;background:#9c9896;border-radius:8px;opacity:.6"></div>
  <div class="abs" role="img" aria-label="magnifying glass illustration" style="left:680px;top:422px;width:68px;height:112px;background:var(--magenta);border-radius:34px 34px 10px 10px;opacity:.85"></div>
  <div class="abs" role="img" aria-label="snowflake doodle" style="left:585px;top:485px;width:90px;height:90px;background:#fdeed0;border-radius:50%"></div>
  <div class="abs" role="img" aria-label="sun doodle" style="left:8px;top:700px;width:70px;height:70px;background:#fbdca8;border-radius:50%"></div>
  <div class="abs" role="img" aria-label="illustration of two children" style="left:110px;top:740px;width:130px;height:90px;background:linear-gradient(90deg,#f5c33b,#f47f24);border-radius:40px;opacity:.85"></div>
  <div class="abs" role="img" aria-label="line drawing of a child drawing on paper" style="left:365px;top:755px;width:175px;height:145px;background:#fde6a2;border-radius:12px"></div>
  <div class="abs" role="img" aria-label="pencil doodle" style="left:400px;top:1080px;width:90px;height:70px;background:#f5a93b;border-radius:10px;opacity:.7"></div>
  <div class="abs" role="img" aria-label="pointing hand icon" style="left:300px;top:1118px;width:56px;height:56px;background:#dcdad9;border-radius:14px"></div>

  <div class="abs what-letters">W<br>H<br>A<br>T<br>?</div>
  <div class="abs tag tag-1">Every child develops</div>
  <div class="abs tag tag-2">at her or his own pace.</div>
  <div class="abs what-line wl-1">A developmental delay is <span class="hl">more</span> than</div>
  <div class="abs what-line wl-2">being ‘a <span class="hl">little behind.”</span> it means</div>
  <div class="abs what-line wl-3">your child is continually</div>
  <div class="abs what-line wl-4"><span class="hl">behind</span> in skills</div>
  <div class="abs what-line wl-5">other kids <span class="hl">his age</span> have.</div>

  <h2 class="abs causes-title">Causes</h2>
  <div class="abs cause k1"><span class="pill">Genetic</span> conditions</div>
  <div class="abs cause k2">complications</div>
  <div class="abs cause k3">in <span class="pill">pregnancy</span></div>
  <div class="abs cause k4">or birth</div>
  <div class="abs cause k5">environmental</div>
  <div class="abs cause k6">issues</div>
  <div class="abs cause k7">other <span class="pill">medical</span></div>
  <div class="abs cause k8">conditions</div>

  <h1 class="abs headline h-child">Your Child</h1>
  <div class="abs headline h-needs">N<br>E<br>E<br>D<br>S</div>
  <div class="abs headline h-help">Your Help</div>

  <div class="abs gdd-box"></div>
  <p class="abs gdd-text"><b>Global</b><br><b>Development</b><br><b>Delay</b> is<br>diagnosed when<br>a child is significantly<br>delayed in <b>two</b><br>or more of the<br><b>FIVE</b><br>developmental<br>realms.</p>
  <ul class="abs realms">
    <li>COGNITIVE</li>
    <li>SOCIAL &amp; EMOTIONAL</li>
    <li>COMMUNICATION</li>
    <li>FINE MOTOR SKILL</li>
    <li>GROSS MOTOR SKILL</li>
  </ul>

  <h2 class="abs wcyd-title">What Can<br>You Do?</h2>
  <p class="abs wcyd-text">Each child is <b>different</b> in their<br>own wonderful way, if we choose<br>to celebrate and <b>understand</b><br>the things that make us <b>unique</b><br>as well as the ones that bring us<br><b>together,</b> we can create a much<br><b>happier</b> and more inclusive<br>environment for all our children.</p>

  <div class="abs concerned">CONCERNED?</div>
  <p class="abs concerned-text"><em>EARLY</em><br><em>INTERVENTION</em><br>programs and<br><em>THERAPIES</em><br>can give many<br>children with<br>a <em>HEAD START</em><br>and allow them<br>to reach their<br>full potential.</p>

  <h3 class="abs info-title">More information &amp; support</h3>
</main>
</body>
</html>
```